Stationary for 2-office law firm with global theme

I need stationary with contact info for two offices. I'd like the same letterhead design to work for printing on stationary and also for digital use in Word. The colors and feel should match the new logo, which is a stylized globe with and "F" in it. I'd also like envelopes with an eye-catching design.

Target Market(s)

U.S. citizens seeking dual citizenship with Italy or Ireland

Industry/Entity Type

Law

Font styles to use
Serif
Sans Serif
Other font styles liked:
• To match the logo?

Colors
0054AA
0677BA
7BADD7
CADEEF
E8F1F8

Requirements
Must have
• Clean, modern design incorporating new logo

```html
<!DOCTYPE html>
<html lang="en">
<head>
<meta charset="utf-8">
<title>Marvento Law Stationery</title>
<link href="https://fonts.googleapis.com/css2?family=Montserrat:wght@600;700&family=Arimo:wght@400&display=swap" rel="stylesheet">
<style>
  :root {
    --backdrop: #adadad;
    --paper: #ffffff;
    --navy: #033b6e;
    --sky: #00aeef;
    --ink: #555555;
    --ink-dark: #444444;
  }
  * { margin: 0; padding: 0; box-sizing: border-box; }
  html, body { width: 1200px; height: 937px; overflow: hidden; }
  body { background: var(--backdrop); position: relative; font-family: "Arimo", Arial, sans-serif; color: var(--ink); }

  .sheet { position: absolute; background: var(--paper); box-shadow: 2px 3px 5px rgba(0,0,0,.35); overflow: hidden; }
  .letterhead { left: 57px; top: 136px; width: 471px; height: 666px; }
  .envelope-back { left: 569px; top: 212px; width: 574px; height: 249px; }
  .envelope-front { left: 569px; top: 484px; width: 574px; height: 249px; }

  .header-band {
    position: absolute; left: 0; top: 0; width: 100%; height: 16px;
    background: linear-gradient(90deg, var(--sky) 0%, var(--navy) 45%, var(--navy) 100%);
  }

  .brand { position: absolute; display: flex; align-items: center; }
  .brand-dot { border-radius: 50%; background: var(--sky); flex: none; }
  .brand-name { font-family: "Montserrat", sans-serif; font-weight: 700; color: var(--navy); line-height: .95; text-align: center; }

  .letterhead .brand { left: 153px; top: 26px; gap: 10px; }
  .letterhead .brand-dot { width: 44px; height: 44px; }
  .letterhead .brand-name { font-size: 19px; }

  .salutation { position: absolute; left: 42px; top: 203px; font-family: "Montserrat", sans-serif; font-weight: 600; font-size: 10.5px; color: var(--ink-dark); }
  .letter-body { position: absolute; left: 42px; top: 238px; width: 390px; font-size: 8.1px; line-height: 9.8px; }
  .letter-body p { margin-bottom: 8.3px; }
  .closing { position: absolute; left: 42px; top: 435px; font-family: "Montserrat", sans-serif; font-weight: 600; font-size: 6px; color: var(--ink-dark); }
  .signature { position: absolute; left: 42px; top: 462px; width: 78px; height: 24px; background: #e6e6e6; border-radius: 3px; }

  .letter-footer { position: absolute; left: 0; right: 0; top: 631px; font-size: 7.6px; line-height: 10.5px; color: var(--ink-dark); }
  .footer-line { display: flex; justify-content: center; align-items: center; gap: 7px; }
  .footer-line .sep { color: var(--sky); }
  .footer-line svg { width: 6px; height: 6px; }

  .flap { position: absolute; left: 0; top: 0; }
  .envelope-back .brand { left: 220px; top: 16px; gap: 8px; }
  .envelope-back .brand-dot { width: 36px; height: 36px; }
  .envelope-back .brand-name { font-size: 16px; }

  .envelope-front .brand { left: 199px; top: 23px; gap: 10px; }
  .envelope-front .brand-dot { width: 47px; height: 47px; }
  .envelope-front .brand-name { font-size: 21px; }
  .return-address { position: absolute; left: 0; right: 0; top: 227px; text-align: center; font-size: 8px; color: var(--ink-dark); }
</style>
</head>
<body>

<section class="sheet letterhead">
  <div class="header-band" role="img" aria-label="Decorative header band in navy and sky blue"></div>
  <div class="brand">
    <span class="brand-dot"></span>
    <span class="brand-name">MARVENTO<br>LAW</span>
  </div>

  <p class="salutation">Dear Mr. Carter,</p>
  <div class="letter-body">
    <p>Lorem ipsum dolor sit amet, consectetuer adipiscing elit, sed diam nonmmy nibh euismod tincidunt ut laor eet dolore magna aliquam erat volutpat. Ut wisi enim ad minim veniam, quis nostrud exerci tationmcorper suscipit lobortis nisl ut aliquip ex ea commodo consequat. Duis autem vel eum iriure dolor in hendrerit in vulputate velit esse molestie consequat, vel illum dolore eu feugiat</p>
    <p>Rorem ipsum dolor sit amet, consectetuer adipiscing elit, sed diam nonmmy nibh euismod tincidunt ut laor eet dolore magna aliquam erat volutpat. Ut wisi enim ad minim veniam, quis nostrud exerci tationmcorper suscipit lobortis nisl ut aliquip ex ea commodo consequat. Duis autem vel eum iriure dolor in hendrerit in vulputate velit esse molest</p>
    <p>Dorem ipsum dolor sit amet, consectetuer adipiscing elit, sed diam nonmmy nibh euismod tincidunt ut laor eet dolore magna aliquam erat volutpat. Ut wisi enim ad minim veniam, quis nostrud exerci tationmcorper suscipit lobortis nisl ut aliquip ex ea commodo consequat. Duis autem vel eum iriure dolor in hendrerit in suscipit lobortis nisl ut aliquip ex ea commodo consequat. Duis autem vel eum iriure dolor in hendrerit in vulputate velit esse molestie consequat, vel illum</p>
    <p>Sorem ipsum dolor sit amet, consectetuer adipiscing elit, sed diam nonmmy nibh euismod tincidunt ut laor eet dolore magna aliquam erat volutpat. Ut wisi enim ad minim veniam, quis nostrud exerci tationmcorper suscipit lobortis nisl ut aliquip ex ea commodo consequat. Duis autem vel eum iriure dolor in</p>
  </div>
  <p class="closing">Sincerely,</p>
  <div class="signature" role="img" aria-label="Handwritten signature of the sender"></div>

  <footer class="letter-footer">
    <div class="footer-line">
      <span>Your address, city, state, ZIP 0000</span><span class="sep">|</span>
      <span><svg viewBox="0 0 10 10"><path d="M2,1 L4,1 L4.8,3.2 L3.6,4.2 Q4.6,6 6,6.6 L7,5.4 L9,6.2 L9,8.4 Q5,9.4 2.4,6.6 Q0.6,4 2,1 Z" fill="var(--sky)"/></svg> 555-014-2100</span>
      <span><svg viewBox="0 0 10 10"><circle cx="5" cy="5" r="4.5" fill="var(--sky)"/></svg>&nbsp; www.marventolaw.com</span>
    </div>
    <div class="footer-line">
      <span>Your address, city, state, ZIP 0000</span><span class="sep">|</span>
      <span><svg viewBox="0 0 10 10"><path d="M2,1 L4,1 L4.8,3.2 L3.6,4.2 Q4.6,6 6,6.6 L7,5.4 L9,6.2 L9,8.4 Q5,9.4 2.4,6.6 Q0.6,4 2,1 Z" fill="var(--sky)"/></svg> 555-014-2100</span>
      <span><svg viewBox="0 0 10 10"><circle cx="5" cy="5" r="4.5" fill="var(--sky)"/></svg>&nbsp; www.marventolaw.com</span>
    </div>
  </footer>
</section>

<section class="sheet envelope-back">
  <svg class="flap" width="574" height="80" viewBox="0 0 574 80">
    <defs>
      <filter id="flap-shadow" x="-5%" y="-20%" width="110%" height="160%">
        <feDropShadow dx="0" dy="3" stdDeviation="3" flood-opacity=".28"/>
      </filter>
    </defs>
    <path d="M2,0 L572,0 L560,48 Q554,69 530,69 L44,69 Q20,69 14,48 Z" fill="var(--paper)" filter="url(#flap-shadow)"/>
  </svg>
  <div class="brand">
    <span class="brand-dot"></span>
    <span class="brand-name">MARVENTO<br>LAW</span>
  </div>
</section>

<section class="sheet envelope-front">
  <div class="header-band" role="img" aria-label="Decorative header band in navy and sky blue"></div>
  <div class="brand">
    <span class="brand-dot"></span>
    <span class="brand-name">MARVENTO<br>LAW</span>
  </div>
  <p class="return-address">Your address, city, state, ZIP 0000</p>
</section>

</body>
</html>
```